Healthcare Industry Needs a Packaging Design for Foot Protective Tape

We need a packaging design for a new company based in Colorado called Pavorins. We have developed a skin conforming foot-shaped protective tape that attaches to the bottom of your foot. Pavorins protects your feet in places where you take off your footwear such as in airport security, locker rooms, yoga studios, and hotels. We would like to see designs that use the color neon green and black (but open to your interpretation). The final design should communicate discreet cleanliness while stylish and fun.

Target Market(s)

US airline travelers, health club users, yoga studios, hotel guests

Industry/Entity Type

Airport

Contact Information for Business Card

Include logo name (PAVORINS), product description (FOOT PROTECTION), company website (www.pavorins.example), social media names (facebook.com/pavorins; twitter.com/pavorins; instagram.com/pavorinsco), Co-founder's name/phone number (Corwin Tadley/555-218-4760)

Logo Text

PAVORINS

Font styles to use
Other font styles liked:
• Anything in Italics would be nice. But we are open to your ideas

Requirements
Must have
• 1. Please see attached word document with packaging description and requests. If any other questions, please let me know.
• 2. (Front of Packaging) Include: Logo name, "Foot Protection", "Antimicrobial", "Eliminate dirty floor phobia"
Nice to have
• 1. Added pictures for reference of the product.
• 2. Facebook, Twitter, and Instagram emblems next to our URLs

```html
<!DOCTYPE html>
<html lang="en">
<head>
<meta charset="utf-8">
<title>Pavorins Label Card Designs</title>
<link href="https://fonts.googleapis.com/css2?family=Source+Sans+3:wght@400;700&family=Open+Sans:wght@400&display=swap" rel="stylesheet">
<style>
  :root {
    --stage: #555555;
    --card: #ffffff;
    --blue: #1a4f9c;
    --green: #1f8f1f;
    --caption: #ffffff;
  }
  * { box-sizing: border-box; margin: 0; padding: 0; }
  html, body { width: 1200px; height: 1000px; overflow: hidden; }
  body { background: var(--stage); position: relative; font-family: "Source Sans 3", sans-serif; }

  .label-card {
    position: absolute; top: 28px; width: 550px; height: 658px;
    background: var(--card); overflow: hidden;
  }
  .label-card--blue { left: 25px; color: var(--blue); }
  .label-card--green { left: 625px; color: var(--green); transform: rotate(180deg); }

  .card-back { position: absolute; inset: 0; transform: rotate(180deg); }

  .directions-title {
    position: absolute; left: 57px; top: 342px; font-size: 19px;
    text-decoration: underline; text-underline-offset: 3px; padding-right: 14px;
  }
  .directions-list { position: absolute; left: 57px; top: 368px; list-style: none; font-size: 17px; line-height: 22px; }
  .directions-list li { display: flex; }
  .directions-list .step { width: 27px; }

  .social { position: absolute; display: flex; align-items: center; gap: 8px; font-size: 17px; }
  .social-mark { width: 18px; height: 18px; background: currentColor; }
  .social-mark--round { border-radius: 50%; }
  .social--fb { left: 72px; top: 520px; }
  .social--tw { left: 243px; top: 520px; }
  .social--pin { left: 72px; top: 556px; }
  .social--ig { left: 243px; top: 556px; }

  .legal { position: absolute; top: 610px; font-size: 14px; font-weight: 700; }
  .legal--proof { left: 57px; }
  .legal--patent { left: 260px; }

  .brand { position: absolute; left: 60px; top: 420px; display: flex; align-items: flex-start; gap: 16px; }
  .brand-dot { width: 96px; height: 96px; border-radius: 50%; background: currentColor; margin-top: 18px; }
  .brand-name { font-size: 84px; line-height: 1; font-weight: 400; margin-top: 14px; }
  .brand-tagline { position: absolute; left: 255px; top: 528px; font-size: 23px; letter-spacing: 0.5px; }

  .flat-card {
    position: absolute; left: 330px; top: 735px; width: 380px; height: 200px;
    background: var(--card); color: var(--blue);
  }
  .flat-card .brand { left: 42px; top: 50px; gap: 10px; }
  .flat-card .brand-dot { width: 56px; height: 56px; margin-top: 8px; }
  .flat-card .brand-name { font-size: 50px; margin-top: 4px; }
  .flat-card .brand-tagline { left: 118px; top: 110px; font-size: 15px; }

  .caption {
    position: absolute; font-family: "Open Sans", sans-serif; color: var(--caption);
    font-size: 29px; transform: translateX(-50%); white-space: nowrap;
  }
  .caption--blue { left: 300px; top: 693px; }
  .caption--green { left: 900px; top: 693px; }
  .caption--card { left: 600px; top: 951px; }
</style>
</head>
<body>

  <section class="label-card label-card--blue">
    <div class="card-back">
      <h2 class="directions-title">Directions</h2>
      <ol class="directions-list">
        <li><span class="step">1.</span>Peel off backing from heel to midsection</li>
        <li><span class="step">2.</span>Apply tape starting at heel</li>
        <li><span class="step">3.</span>Peel off rest of backing towards toes</li>
        <li><span class="step">4.</span>Apply tape stretching towards toes to base of toenails</li>
        <li><span class="step">5.</span>Rub tape to activate adhesive</li>
      </ol>
      <div class="social social--fb"><span class="social-mark"></span>/pavorins</div>
      <div class="social social--tw"><span class="social-mark social-mark--round"></span>@pavorins</div>
      <div class="social social--pin"><span class="social-mark social-mark--round"></span>/pavorinsco</div>
      <div class="social social--ig"><span class="social-mark"></span>/pavorinsco</div>
      <p class="legal legal--proof">NOT CLINICALLY PROVEN.</p>
      <p class="legal legal--patent">PATENTS PENDING</p>
    </div>
    <div class="brand"><span class="brand-dot"></span><span class="brand-name">Pavorins</span></div>
    <p class="brand-tagline">FOOT PROTECTION</p>
  </section>

  <section class="label-card label-card--green">
    <div class="card-back">
      <h2 class="directions-title">Directions</h2>
      <ol class="directions-list">
        <li><span class="step">1.</span>Peel off backing from heel to midsection</li>
        <li><span class="step">2.</span>Apply tape starting at heel</li>
        <li><span class="step">3.</span>Peel off rest of backing towards toes</li>
        <li><span class="step">4.</span>Apply tape stretching towards toes to base of toenails</li>
        <li><span class="step">5.</span>Rub tape to activate adhesive</li>
      </ol>
      <div class="social social--fb"><span class="social-mark"></span>/pavorins</div>
      <div class="social social--tw"><span class="social-mark social-mark--round"></span>@pavorins</div>
      <div class="social social--pin"><span class="social-mark social-mark--round"></span>/pavorinsco</div>
      <div class="social social--ig"><span class="social-mark"></span>/pavorinsco</div>
      <p class="legal legal--proof">NOT CLINICALLY PROVEN.</p>
      <p class="legal legal--patent">PATENTS PENDING</p>
    </div>
    <div class="brand"><span class="brand-dot"></span><span class="brand-name">Pavorins</span></div>
    <p class="brand-tagline">FOOT PROTECTION</p>
  </section>

  <p class="caption caption--blue">Blue design</p>
  <p class="caption caption--green">Green design</p>

  <section class="flat-card">
    <div class="brand"><span class="brand-dot"></span><span class="brand-name">Pavorins</span></div>
    <p class="brand-tagline">FOOT PROTECTION</p>
  </section>

  <p class="caption caption--card">Pavorins Product label card (to be folded onto package)</p>

</body>
</html>
```